Systemischer Coach sucht Flyer-Design
Zielgruppe
Ich bin systemischer Coach und gebe Einzelcoaching in einem sehr schönen Coaching Raum in Aachen.
Meine Zielgruppe sind Menschen im Alter von 28-50, die ehrgeizig, selbstbestimmt und modern sind und sich gerne weiterentwickeln möchten.
Zentrale Themen sind:
Motivation
Persönlichkeitsentwicklung
Ziel- und Entscheidungsfindung
Selbst-/Zeitmanagement
Selbstbewusstsein stärken
Work-Life-Balance
Stressmanagement
Coaching ist professioneller, individueller Begleitprozess für Menschen in herausfordernden Berufs- und Lebenssituationen. Im Rahmen eines systemischen und humanistischen Verständnisses wird der Klient dabei unterstützt, eigenständig konstruktive und nachhaltige Lösungen zu erarbeiten. Das Coaching findet in geschütztem Rahmen statt, Coach und Klient begegnen sich auf Augenhöhe. Der Klient ist Experte für die Inhalte, der Coach ist Experte für Prozess und Struktur
Aufgabenstellung
Farben
schwarz/gold
Vorderseite schlichte/kräftige Symbole und Motto 'Feel the flow'
Rückseite: Text
Text:
'Feel the Flow'
Ist es Zeit,
Deine Stärken zu entdecken?
Deine Ressourcen zu reaktivieren?
Work und Life wieder in Balance zu bringen?
für etwas mehr Motivation und Inspiration?
Suchst Du,
Mut, um Deine Ziele zu erreichen?
Wege, um den Stress links liegen zu lassen?
Selbstbewusstsein für ein sicheres Auftreten?
Struktur und Klarheit im Job?
Bring Flow in Dein Leben!
Als Coach begleite ich Dich auf Deinem Weg zum Ziel

```html
<!DOCTYPE html>
<html lang="de">
<head>
<meta charset="utf-8">
<title>Systemisches Coaching – Flyer</title>
<link rel="stylesheet" href="https://fonts.googleapis.com/css2?family=Montserrat:wght@300;400;600;700&family=Questrial&family=Nothing+You+Could+Do&display=swap">
<style>
  :root {
    --frame: #2b2b2b;
    --ground: #141414;
    --gold: #d6a64a;
    --gold-dark: #a8732f;
    --gold-light: #f2c766;
    --white: #ffffff;
  }
  * { margin: 0; padding: 0; box-sizing: border-box; }
  html, body {
    width: 1200px; height: 433px; overflow: hidden;
    background: var(--frame);
  }
  .flyer {
    position: relative;
    width: 1200px; height: 433px;
    background: var(--ground);
    border: 8px solid var(--frame);
  }
  .questions {
    position: absolute; left: 56px; top: 27px;
    font-family: "Questrial", sans-serif;
    font-size: 20.5px; line-height: 29.2px;
    color: var(--gold);
    letter-spacing: 0.4px;
  }
  .questions p + p { margin-top: 29px; }
  .motto {
    position: absolute; left: 56px; top: 344px;
    font-family: "Nothing You Could Do", cursive;
    font-size: 29px; color: var(--gold);
  }
  .divider {
    position: absolute; left: 622px; top: 30px;
    width: 3px; height: 348px; background: var(--gold);
  }
  .headline {
    position: absolute; right: 57px; top: 40px;
    text-align: right;
    font-family: "Montserrat", sans-serif;
    font-weight: 700; font-size: 37px; line-height: 39px;
    letter-spacing: 2.4px; text-transform: uppercase;
    background: linear-gradient(100deg, var(--gold-dark), var(--gold-light) 60%, var(--gold));
    -webkit-background-clip: text; background-clip: text;
    color: transparent;
  }
  .contact {
    position: absolute; right: 57px; top: 252px;
    text-align: right;
    font-family: "Montserrat", sans-serif;
    color: var(--white); font-size: 19px; line-height: 27px;
    letter-spacing: 0.8px;
  }
  .contact .name, .contact .offer { font-weight: 700; }
  .contact .role, .contact .mail { font-weight: 400; }
  .contact .offer { margin-top: 28px; }
</style>
</head>
<body>
  <main class="flyer">
    <section class="questions">
      <p>Ist es Zeit,<br>Deine Stärken zu entdecken?<br>Deine Ressourcen zu reaktivieren?<br>Work und Life wieder in Balance zu bringen?<br>für etwas mehr Motivation und Inspiration?</p>
      <p>Suchst Du,<br>Mut, um Deine Ziele zu erreichen?<br>Wege, um den Stress links liegen zu lassen?<br>Selbstbewusstsein für ein sicheres Auftreten?<br>Struktur und Klarheit im Job?</p>
    </section>
    <p class="motto">Bring Flow in Dein Leben!</p>
    <div class="divider"></div>
    <h1 class="headline">Als Coach<br>begleite<br>ich Dich auf<br>Deinem Weg<br>zum Ziel</h1>
    <section class="contact">
      <p class="name">Berthold Winsper</p>
      <p class="role">systemisches Coaching</p>
      <p class="offer">kostenloses Erstgespräch:</p>
      <p class="mail">bwcoaching@postfach.de</p>
    </section>
  </main>
</body>
</html>
```